Advertisement flyer for fire sprinkler repair parts. The projected audience are contractors.

I need a flyer advertising specific parts that we are stocking at our company "Northgate Valve Supply." I have attached a picture of our logo. I want the title to say "Fire Pump Repair Parts and Accessories." I want to specifically advertise the following parts: Repack Kits and Repair Parts, Jockey Pumps, Pump Controllers, Casing Relief Valves, Air Release Valves, Suction/Discharge Gauges, Pump Shaft Couplers & Shim Kits, Fire Pump Relief Valves, and UL Listed Pressure Reducing Valves. I have attached pictures of the manufacturers I want to advertise on this flyer. I have also attached pictures of some of the parts we are stocking that I would like to be included somewhere in the flyer. I would like all of the pictures to have a transparent background. Also I would like our phone number :(800)-482-3067, and our website www.ridgeflowsupply.com included. I made my own design that I have Attached. You do not have to go based off this design, but I would like the basic content to be the same. We do have Same- Day shipping as well as Free Tech Support if you can include that anywhere.

```html
<!DOCTYPE html>
<html lang="en">
<head>
<meta charset="utf-8">
<title>Fire Pump Repair Parts and Accessories – Northgate Valve Supply</title>
<link rel="stylesheet" href="https://fonts.googleapis.com/css2?family=Open+Sans:wdth,wght@75..100,400;75..100,600;75..100,700&family=Roboto:wght@400;500&display=swap">
<style>
  :root {
    --magenta: #d62a5e;
    --violet: #8a4ea0;
    --royal: #3b4fb0;
    --navy: #1f2d5c;
    --red-dot: #e3174b;
    --ink: #3a3f52;
    --paper: #ffffff;
    --stage: #f2f2f2;
    --rule: #c9c9cf;
  }
  * { box-sizing: border-box; margin: 0; padding: 0; }
  html, body { width: 1200px; height: 1200px; overflow: hidden; background: var(--stage); }
  .canvas { position: relative; width: 1200px; height: 1200px; }
  .flyer {
    position: absolute; left: 204px; top: 40px;
    width: 836px; height: 1184px;
    transform: scale(0.946); transform-origin: 0 0;
    background: var(--paper); overflow: hidden;
    font-family: "Open Sans", sans-serif;
  }
  .abs { position: absolute; }
  .backdrop { left: 0; top: 0; }
  .photo-scene { left: 0; top: 200px; width: 836px; height: 380px;
    background: linear-gradient(180deg, #b9aaa6 0%, #a8393c 45%, #c81f25 70%, #7e1e1f 100%); }

  .title { left: 0; width: 836px; top: 48px; text-align: center; color: #fff; }
  .title-rule { width: 642px; height: 6px; margin: 0 auto; border-top: 2px solid #fff; border-bottom: 1px solid #fff; }
  .title-main { font-weight: 700; font-stretch: 92%; font-size: 70px; line-height: 72px; margin-top: 2px; }
  .title-sub { font-weight: 700; font-stretch: 92%; font-size: 51px; line-height: 50px; margin-bottom: 8px; }

  .parts-list { left: 44px; top: 586px; list-style: none; }
  .parts-list li { position: relative; padding-left: 26px; font-size: 16.5px; font-weight: 600; color: var(--ink); height: 32.4px; line-height: 24px; white-space: nowrap; }
  .parts-list li::before { content: ""; position: absolute; left: 2px; top: 8px; width: 9px; height: 9px; border-radius: 50%; background: var(--red-dot); }

  .product-shot { border-radius: 14px; }
  .shot-kit { left: 330px; top: 536px; width: 290px; height: 222px; background: linear-gradient(160deg, #2c4fc2 0%, #9aa3b8 60%, #e8e9ee 100%); }
  .shot-valve { left: 628px; top: 562px; width: 74px; height: 146px; background: linear-gradient(180deg, #c9a25e, #8f6b33); }
  .shot-pump { left: 712px; top: 620px; width: 92px; height: 272px; background: linear-gradient(180deg, #e8d3a6 0%, #b9bfc8 45%, #2f5fa8 100%); }
  .shot-gaskets { left: 426px; top: 770px; width: 228px; height: 130px; background: linear-gradient(135deg, #9b8577, #d8d3d0); }

  .divider { left: 44px; top: 914px; width: 748px; border-top: 1px solid var(--rule); }

  .maker { font-weight: 700; font-size: 15px; white-space: nowrap; width: 160px; text-align: center; }
  .maker-a { color: var(--navy); }
  .maker-b { color: var(--royal); }
  .maker-c { color: var(--red-dot); }

  .brand { left: 0; width: 836px; top: 1054px; text-align: center; font-family: "Roboto", sans-serif; color: var(--royal); }
  .brand-name { font-size: 38px; line-height: 40px; }
  .brand-tag { font-size: 18px; line-height: 22px; }

  .contact-call { left: 43px; top: 1143px; color: #fff; font-weight: 700; font-size: 16px; display: flex; align-items: center; gap: 6px; white-space: nowrap; }
  .contact-web { left: 420px; top: 1139px; width: 380px; text-align: center; color: #fff; font-weight: 600; font-size: 16px; letter-spacing: 3px; white-space: nowrap; }
</style>
</head>
<body>
<div class="canvas">
  <article class="flyer">
    <div class="abs photo-scene" role="img" aria-label="Photo of a fire pump room with red pumps, valves and piping"></div>

    <svg class="abs backdrop" width="836" height="1184" viewBox="0 0 836 1184" aria-hidden="true">
      <defs>
        <linearGradient id="headerFill" x1="0" y1="0" x2="1" y2="0">
          <stop offset="0" stop-color="#d62a5e"/>
          <stop offset="0.5" stop-color="#8a4ea0"/>
          <stop offset="1" stop-color="#d62a5e"/>
        </linearGradient>
        <linearGradient id="headerShade" x1="0" y1="0" x2="0" y2="1">
          <stop offset="0" stop-color="#d62a5e" stop-opacity="0"/>
          <stop offset="0.55" stop-color="#d62a5e" stop-opacity="1"/>
        </linearGradient>
      </defs>
      <path d="M0 0 H836 V200 Q430 265 0 224 Z" fill="#3b4fb0"/>
      <path d="M0 0 H836 V160 Q420 265 0 178 Z" fill="url(#headerFill)"/>
      <path d="M0 0 H836 V160 Q420 265 0 178 Z" fill="url(#headerShade)"/>
      <path d="M0 536 Q400 485 836 562 V1184 H0 Z" fill="#3b4fb0"/>
      <path d="M0 584 Q400 505 836 575 V1184 H0 Z" fill="#ffffff"/>
      <path d="M0 1132 H836 V1184 H0 Z" fill="#3b4fb0"/>
      <path d="M355 1132 H836 V1170 H378 Z" fill="#ffffff"/>
      <path d="M361 1132 H836 V1166 H382 Z" fill="#e3174b"/>
    </svg>

    <header class="abs title">
      <div class="title-rule"></div>
      <h1 class="title-main">FIRE PUMP REPAIR</h1>
      <p class="title-sub">PARTS AND ACCESSORIES</p>
      <div class="title-rule"></div>
    </header>

    <ul class="abs parts-list">
      <li>Fire Pump Repack Kits</li>
      <li>Jockey Pumps</li>
      <li>Pump Controllers</li>
      <li>Casing Relief Valves</li>
      <li>Air Release Valves</li>
      <li>Suction / Discharge Gauges</li>
      <li>Packing Tools</li>
      <li>Pump Shaft Couplers &amp; Shim Kits</li>
      <li>Fire Pump Relief Valves</li>
      <li>UL Listed Pressure Reducing Valves</li>
    </ul>

    <div class="abs product-shot shot-kit" role="img" aria-label="Blue packing tool case with packing hooks and tools"></div>
    <div class="abs product-shot shot-valve" role="img" aria-label="Brass pressure reducing valve"></div>
    <div class="abs product-shot shot-pump" role="img" aria-label="Vertical multistage jockey pump"></div>
    <div class="abs product-shot shot-gaskets" role="img" aria-label="Pump casing gaskets, hardware and packing rings"></div>

    <div class="abs divider"></div>

    <div class="abs maker maker-a" style="left:46px; top:944px;">Orvane Pumps</div>
    <div class="abs maker maker-b" style="left:246px; top:944px;">Harwell Drive</div>
    <div class="abs maker maker-b" style="left:446px; top:944px;">Talvane Pump</div>
    <div class="abs maker maker-a" style="left:646px; top:944px;">Nordvik</div>
    <div class="abs maker maker-a" style="left:46px; top:1008px;">Vantor Valve</div>
    <div class="abs maker maker-c" style="left:246px; top:1008px;">Blazewick</div>
    <div class="abs maker maker-b" style="left:446px; top:1008px;">Corra Pumps</div>
    <div class="abs maker maker-a" style="left:646px; top:1008px;">Lindqvist</div>

    <div class="abs brand">
      <div class="brand-name">Northgate Valve</div>
      <div class="brand-tag">Supply Company</div>
    </div>

    <div class="abs contact-call">
      <span>Call Us Today !</span>
      <svg width="14" height="14" viewBox="0 0 24 24" aria-hidden="true"><path fill="#fff" d="M6.6 10.8a15.1 15.1 0 0 0 6.6 6.6l2.2-2.2c.3-.3.7-.4 1-.2 1.1.4 2.3.6 3.6.6.6 0 1 .4 1 1V20c0 .6-.4 1-1 1A17 17 0 0 1 3 4c0-.6.4-1 1-1h3.5c.6 0 1 .4 1 1 0 1.3.2 2.5.6 3.6.1.3 0 .7-.2 1z"/></svg>
      <span>(800)-482-3067</span>
    </div>
    <div class="abs contact-web">www.ridgeflowsupply.com</div>
  </article>
</div>
</body>
</html>
```